Business Card for Wellness Clinic

We need a business card for our new logo. I want it to match the feel of the logo

Target Market(s)

Young professional families looking for holistic health care

Industry/Entity Type

Health And Wellness

Contact Information for Business Card

Our business Name: Larkvale Health & wellness Centre, our phone #, email address...see attached old business card

Font styles to use
Sans Serif

Colors
33b8a4
cee9f5

Requirements
Must have
• my logo and business name
• Font is "Helvetica Neue LT Std 45 Light" and
• Only for "&" using font "Trajan pro bold"
• Use colors in the logo

```html
<!DOCTYPE html>
<html lang="en">
<head>
<meta charset="utf-8">
<title>Larkvale Health &amp; Wellness Centre – Business Card</title>
<link rel="stylesheet" href="https://fonts.googleapis.com/css2?family=Roboto:wght@300&family=PT+Sans:wght@400;700&display=swap">
<style>
  :root {
    --backdrop: #ece8e2;
    --kraft: #c9a77b;
    --kraft-light: #d3b387;
    --ink: #111111;
    --rule: #6e5a40;
  }
  * { box-sizing: border-box; margin: 0; padding: 0; }
  html, body { width: 1200px; height: 900px; overflow: hidden; }
  body {
    position: relative;
    background: var(--backdrop);
    color: var(--ink);
    font-family: "PT Sans", sans-serif;
  }
  .card {
    position: absolute;
    height: 342px;
    background: linear-gradient(135deg, var(--kraft-light), var(--kraft));
    box-shadow: 0 6px 18px rgba(0,0,0,0.18);
  }
  .card--front { left: 238px; top: 62px; width: 555px; }
  .card--back  { left: 458px; top: 518px; width: 559px; }

  .front-content {
    position: absolute; inset: 0;
    display: flex; flex-direction: column; align-items: center;
  }
  .brand-mark {
    width: 56px; height: 56px;
    margin-top: 42px;
    background: var(--ink);
  }
  .brand-name {
    margin-top: 16px;
    font-family: "Roboto", sans-serif;
    font-weight: 300;
    font-size: 22px;
    letter-spacing: 3.2px;
    line-height: 1;
    text-transform: uppercase;
  }
  .brand-amp {
    font-family: "Roboto", sans-serif;
    font-weight: 300;
    font-size: 9px;
    line-height: 1;
    margin-top: 3px;
    margin-left: 0;
    display: flex; align-items: center; gap: 8px;
  }
  .brand-amp::after {
    content: ""; display: block; width: 90px; height: 1px; background: var(--rule);
  }
  .brand-sub {
    font-family: "Roboto", sans-serif;
    font-weight: 300;
    font-size: 11.5px;
    letter-spacing: 6.4px;
    line-height: 1;
    margin-top: 1px;
    text-transform: uppercase;
  }
  .person-name {
    margin-top: 22px;
    font-weight: 700;
    font-size: 18px;
    line-height: 1.1;
  }
  .person-role {
    font-size: 15px;
    line-height: 1.3;
  }
  .contact-list {
    list-style: none;
    margin-top: 14px;
    display: flex; flex-direction: column; align-items: center; gap: 2px;
    font-size: 15px;
    line-height: 18px;
  }
  .contact-list li { display: flex; align-items: center; gap: 6px; }
  .contact-icon { width: 12px; height: 12px; fill: var(--ink); }

  .back-content {
    position: absolute; inset: 0;
    display: flex; align-items: center; justify-content: center; gap: 16px;
  }
  .back-mark { width: 44px; height: 44px; background: var(--ink); }
  .back-name {
    font-family: "Roboto", sans-serif;
    font-weight: 300;
    font-size: 30px;
    letter-spacing: 4px;
    text-transform: uppercase;
  }
</style>
</head>
<body>
  <section class="card card--front" aria-label="Business card front">
    <div class="front-content">
      <div class="brand-mark" aria-hidden="true"></div>
      <h1 class="brand-name">Larkvale Health</h1>
      <div class="brand-amp">&amp;</div>
      <div class="brand-sub">Wellness Centre</div>
      <p class="person-name">Daniel Harper</p>
      <p class="person-role">Managing Director</p>
      <ul class="contact-list">
        <li>
          <svg class="contact-icon" viewBox="0 0 24 24" aria-hidden="true"><path d="M6.6 10.8a15.1 15.1 0 0 0 6.6 6.6l2.2-2.2c.3-.3.7-.4 1-.2 1.1.4 2.3.6 3.6.6.6 0 1 .4 1 1V20c0 .6-.4 1-1 1A17 17 0 0 1 3 4c0-.6.4-1 1-1h3.5c.6 0 1 .4 1 1 0 1.3.2 2.5.6 3.6.1.3 0 .7-.2 1z"/></svg>
          044-987 650 312
        </li>
        <li>
          <svg class="contact-icon" viewBox="0 0 24 24" aria-hidden="true"><path d="M2 5h20v14H2z M2 5l10 8 10-8" fill="var(--ink)" stroke="var(--kraft)" stroke-width="1.5"/></svg>
          info@larkvalemail.com
        </li>
        <li>
          <svg class="contact-icon" viewBox="0 0 24 24" aria-hidden="true"><circle cx="12" cy="12" r="11"/><path d="M1 12h22M12 1c3 3 3 19 0 22M12 1c-3 3-3 19 0 22" fill="none" stroke="var(--kraft)" stroke-width="1.5"/></svg>
          www.larkvalehealth.com
        </li>
      </ul>
    </div>
  </section>

  <section class="card card--back" aria-label="Business card back">
    <div class="back-content">
      <div class="back-mark" aria-hidden="true"></div>
      <p class="back-name">Larkvale</p>
    </div>
  </section>
</body>
</html>
```